Card Design Project

We are looking for a couple card / box designs that will for a new company that is in the bereavement assistance industry.
Our customers are churches, counseling centers and funeral homes.
Once we have these card designs we will need to work with that same artist to help us out with box graphic designs that are similar to the card designs. The box is 12" long x 4" wide x 6" high
We will need more designs in the future so we are looking for an artist for future work.
Our look needs to be professional and solemn.
The front of the card should be quite close to what i am attaching but with some professional touches to it that give it a proper look. We dont want you to stray to far from what i have attached but if you feel you have some good ideas we would be more than happy to see them.
The back of the card we want people to be able to leave the family a note so will need wording such as "leave a message to the family" or "write a memory"
Keep in mind we will need this look to be able to match graphics on the box as well, we kind of need the card design and box design to go together.
Thanks
Just wanted to mention to all designers that although we would like our logo on the card it is something that we need to keep kind of in the background somehow. We cant be seen as trying to push a brand name too much so please keep that in mind. Thanks
Reason: HOLIDAY
Designers, I took the need to see what the design looked like on a box out.
Reason: just need a bit of extra time guys, thanks for all who are helping us on this!
Target Market(s)
Funeral homes, churches, counseling centers
Industry/Entity Type
Industry
Requirements
Must have
- Professional and solemn look
Card need to be 4"wide X 6" high and needs to be portrait
A pin will be attached to the top right part of the card so will need a space there for it.
I was thinking that we would have the pic of the ribbon symbol there so when the pin is off the card there would still be a ribbon pic there. The pins that we will be attaching are ribbon pins similar to what i have on my pdf's
Please keep in mind that we cant really have out logo in a dominant area on the card. We would like to have it subtly in there but not to where it is in your face type of thing.
Nice to have
- Our logo but very small, not to intrusive .
Would like 2 designs, one dark and another light.
Maybe 1 masculine or gender neutral and another feminine
Wording should be the same

```html
<!DOCTYPE html>
<html lang="en">
<head>
<meta charset="utf-8">
<title>Memorial Card – Front and Back</title>
<link rel="stylesheet" href="https://fonts.googleapis.com/css2?family=Eagle+Lake&display=swap">
<style>
  :root {
    --paper: #ffffff;
    --ink: #111111;
    --frame: #000000;
    --rule: #7a7a7a;
    --rule-light: #a9a9a9;
    --ornament: #1a1a1a;
    --ribbon: #3a3a3a;
  }
  * { margin: 0; padding: 0; box-sizing: border-box; }
  html, body {
    width: 1200px; height: 854px; overflow: hidden;
    background: var(--paper);
  }
  .canvas { position: relative; width: 1200px; height: 854px; background: var(--paper); }

  .card {
    position: absolute; top: 15px;
    border: 1.5px solid var(--frame);
    background: var(--paper);
  }
  .card--front { left: 14px; width: 541px; height: 813px; }
  .card--back  { left: 638px; width: 542px; height: 812px; }

  .frame { position: absolute; left: 0; top: 0; }

  .ornament {
    position: absolute; background: var(--ornament);
    border-radius: 14px;
  }
  .ornament--top    { left: 60px; top: 10px; width: 420px; height: 44px; }
  .ornament--bottom { left: 60px; top: 757px; width: 420px; height: 44px; }

  .ribbon {
    position: absolute; left: 401px; top: 69px; width: 96px; height: 122px;
    background: var(--ribbon); border-radius: 40px 40px 8px 8px;
  }

  .greeting {
    position: absolute; left: 148px; top: 130px;
    font-family: "Eagle Lake", serif; font-size: 33px; font-weight: 400;
    line-height: 40px; color: var(--ink); white-space: nowrap;
  }

  .message {
    position: absolute; left: 0; width: 538px; text-align: center;
    font-family: "Helvetica Neue", Helvetica, Arial, sans-serif;
    font-size: 19px; line-height: 34px; color: var(--ink);
  }
  .message--support { top: 239px; }
  .message--touched { top: 341px; }
  .message--pin     { top: 443px; }
  .message--thanks  { top: 647px; }

  .divider { position: absolute; left: 65px; width: 413px; height: 22px; }
  .divider__rule {
    position: absolute; left: 0; right: 0; top: 10px; height: 2px;
    background: var(--rule-light);
  }
  .divider__mark {
    position: absolute; left: 172px; top: 0; width: 70px; height: 22px;
    background: var(--ornament); border-radius: 10px;
  }
  .divider--one   { top: 311px; }
  .divider--two   { top: 418px; }
  .divider--three { top: 602px; }

  .memory-title {
    position: absolute; left: 41px; top: 207px;
    font-family: "Eagle Lake", serif; font-size: 21px; font-weight: 400;
    line-height: 30px; color: var(--ink); white-space: nowrap;
  }
  .memory-lines { position: absolute; left: 0; top: 0; }
</style>
</head>
<body>
<main class="canvas">

  <section class="card card--front" aria-label="Card front">
    <svg class="frame" width="541" height="813" viewBox="0 0 541 813" aria-hidden="true">
      <rect x="22" y="48" width="496" height="720" fill="none" stroke="var(--frame)" stroke-width="4"/>
      <rect x="29" y="55" width="482" height="706" fill="none" stroke="var(--frame)" stroke-width="1"/>
    </svg>
    <div class="ornament ornament--top" role="img" aria-label="Black scrollwork flourish along the top edge"></div>
    <div class="ornament ornament--bottom" role="img" aria-label="Black scrollwork flourish along the bottom edge"></div>

    <h1 class="greeting">Dear Friends</h1>
    <div class="ribbon" role="img" aria-label="Dark grey awareness ribbon where the pin is attached"></div>

    <p class="message message--support">Your support in attending this memorial<br>and celebration of life means so much to us.</p>
    <div class="divider divider--one"><span class="divider__rule"></span><span class="divider__mark" role="img" aria-label="Small scroll divider ornament"></span></div>

    <p class="message message--touched">Our loved one has touched you in ways<br>we may not even recognize yet.</p>
    <div class="divider divider--two"><span class="divider__rule"></span><span class="divider__mark" role="img" aria-label="Small scroll divider ornament"></span></div>

    <p class="message message--pin">We invite you to wear this pin through<br>your grieving process, which we receive as<br>a symbol of your sympathy and support<br>of our loss.</p>
    <div class="divider divider--three"><span class="divider__rule"></span><span class="divider__mark" role="img" aria-label="Small scroll divider ornament"></span></div>

    <p class="message message--thanks">Thank you for grieving together with us</p>
  </section>

  <section class="card card--back" aria-label="Card back">
    <h2 class="memory-title">Write a memory</h2>
    <svg class="memory-lines" width="542" height="812" viewBox="0 0 542 812" aria-hidden="true">
      <g stroke="var(--rule)" stroke-width="1">
        <line x1="252" y1="226" x2="514" y2="226"/>
        <line x1="37" y1="258" x2="514" y2="258"/>
        <line x1="37" y1="290" x2="514" y2="290"/>
        <line x1="37" y1="322" x2="514" y2="322"/>
        <line x1="37" y1="354" x2="514" y2="354"/>
        <line x1="37" y1="386" x2="514" y2="386"/>
        <line x1="37" y1="418" x2="514" y2="418"/>
        <line x1="37" y1="450" x2="514" y2="450"/>
        <line x1="37" y1="482" x2="514" y2="482"/>
        <line x1="37" y1="514" x2="514" y2="514"/>
        <line x1="37" y1="546" x2="514" y2="546"/>
        <line x1="37" y1="578" x2="514" y2="578"/>
        <line x1="37" y1="610" x2="514" y2="610"/>
        <line x1="37" y1="642" x2="514" y2="642"/>
        <line x1="37" y1="674" x2="514" y2="674"/>
      </g>
    </svg>
  </section>

</main>
</body>
</html>
```